New business card for civil engineering company - "Keystone Audit"

We need a business card designed for our new structural engineering company.

The company name is "Keystone Audit" logo files attached.

We would like the following:
* Two-sided card
* Simple design

Information to be placed on the card:
Name - Marcus Dellow
Job Title - Director / Structural Engineer
Credentials - BEng(Hons), CPEng, CMengNZ, IntPE(NZ)
Email - marcus.dellow@keystoneaudit.co.nz
mobile - 0219364058
website - www.keystoneaudit.co.nz

```html
<!DOCTYPE html>
<html lang="en">
<head>
<meta charset="utf-8">
<title>Keystone Audit – Business Card</title>
<link rel="stylesheet" href="https://fonts.googleapis.com/css2?family=Arimo:wght@400;700&display=swap">
<style>
  :root {
    --page: #ffffff;
    --navy: #1f4263;
    --ink-light: #ffffff;
    --ghost: rgba(255, 255, 255, 0.045);
  }
  html, body {
    margin: 0;
    padding: 0;
    width: 1200px;
    height: 1200px;
    overflow: hidden;
    background: var(--page);
  }
  .canvas {
    position: relative;
    width: 1200px;
    height: 1200px;
    font-family: "Arimo", Arial, sans-serif;
    color: var(--ink-light);
  }
  .card {
    position: absolute;
    left: 112px;
    width: 965px;
    height: 551px;
    background: var(--navy);
    border-radius: 38px;
    overflow: hidden;
  }
  .card--front { top: 34px; }
  .card--back { top: 618px; }

  .text { position: absolute; margin: 0; line-height: 1; white-space: nowrap; }

  /* front */
  .brand-lockup {
    position: absolute; left: 64px; top: 438px;
    width: 200px;
  }
  .brand-name {
    position: static; display: block;
    font-size: 18px; font-weight: 700; letter-spacing: 0.05em;
  }
  .brand-tagline {
    position: static; display: block; margin-top: 8px;
    font-size: 9px; font-weight: 700; letter-spacing: 0.2em;
  }
  .front-divider {
    position: absolute; left: 292px; top: 428px;
    width: 2px; height: 59px; background: var(--ink-light);
  }
  .web-pill {
    position: absolute; left: 337px; top: 436px; right: 0; height: 39px;
    background: var(--ink-light);
    border-radius: 20px 0 0 20px;
  }
  .web-pill__text {
    left: 40px; top: 9px;
    font-size: 23px; font-weight: 700; letter-spacing: 0.1em;
    color: var(--navy);
  }

  /* back */
  .ghost-mark {
    position: absolute; left: 0; top: 0;
    width: 965px; height: 551px;
  }
  .ghost-mark text { fill: var(--ghost); font-family: "Arimo", Arial, sans-serif; }
  .ghost-mark__name { font-weight: 700; }
  .ghost-mark__tagline { font-weight: 400; }
  .person-name {
    left: 58px; top: 280px;
    font-size: 44px; font-weight: 700; letter-spacing: 0.06em;
  }
  .person-role {
    left: 58px; top: 321px;
    font-size: 22px; font-weight: 700; letter-spacing: 0.06em;
  }
  .person-credentials {
    left: 58px; top: 347px;
    font-size: 22px; font-weight: 700; letter-spacing: 0.06em;
  }
  .back-rule {
    position: absolute; left: 58px; top: 386px;
    width: 851px; height: 2px; background: var(--ink-light);
  }
  .contact {
    left: 76px;
    font-size: 24px; font-weight: 700; letter-spacing: 0.08em;
  }
  .contact--email { top: 418px; }
  .contact--phone { top: 453px; }
  .contact--web { top: 488px; }
  .contact__label { display: inline-block; width: 36px; }
  .back-bar {
    position: absolute; left: 535px; top: 490px; right: 0; height: 17px;
    background: var(--ink-light);
    border-radius: 9px 0 0 9px;
  }
</style>
</head>
<body>
<main class="canvas">
  <section class="card card--front" aria-label="Card front">
    <div class="brand-lockup">
      <p class="text brand-name">KEYSTONE AUDIT</p>
      <p class="text brand-tagline">PEER REVIEW SPECIALISTS</p>
    </div>
    <div class="front-divider"></div>
    <div class="web-pill">
      <p class="text web-pill__text">www.keystoneaudit.co.nz</p>
    </div>
  </section>

  <section class="card card--back" aria-label="Card back">
    <svg class="ghost-mark" viewBox="0 0 965 551" aria-hidden="true">
      <text class="ghost-mark__name" x="25" y="133" font-size="112" textLength="920" lengthAdjust="spacingAndGlyphs">KEYSTONE AUDIT</text>
      <text class="ghost-mark__tagline" x="25" y="219" font-size="48" textLength="920" lengthAdjust="spacing">PEER REVIEW SPECIALISTS</text>
    </svg>
    <p class="text person-name">Marcus Dellow</p>
    <p class="text person-role">Director/Structural Engineer</p>
    <p class="text person-credentials">BEng(Hons),CPEng,CMengNZ,IntPE(NZ)</p>
    <div class="back-rule"></div>
    <p class="text contact contact--email"><span class="contact__label">e:</span>marcus.dellow@keystoneaudit.co.nz</p>
    <p class="text contact contact--phone"><span class="contact__label">t :</span>0219364058</p>
    <p class="text contact contact--web"><span class="contact__label">w:</span>www.keystoneaudit.co.nz</p>
    <div class="back-bar"></div>
  </section>
</main>
</body>
</html>
```